20 year old business card needs re-design

We need to redesign our corporate business card look. We need something that appears more modern, eye catchy but professional.

Target Market(s)

manufacturing industry

Industry/Entity Type

Manufacturer

Contact Information for Business Card

One side can have the logo. Other side can have contact information.

Font styles to use
Serif

Colors
3277b5
33b8a4
ffffff

Requirements
Must have
• Eye catchy - need to standout from the crowd. company logo cannot change. Full name, job title, phone number and email address.
Should not have
• Fax, business address is not necessary.

```html
<!DOCTYPE html>
<html lang="en">
<head>
<meta charset="utf-8">
<title>Forgeline International – Business Card</title>
<link rel="stylesheet" href="https://fonts.googleapis.com/css2?family=Libre+Franklin:wght@400;600;800&display=swap">
<style>
  :root {
    --page: #e6e7ea;
    --blue-deep: #2a55ad;
    --blue-mid: #3a6fc2;
    --blue-brand: #3277b5;
    --ink: #1c1c1f;
    --ink-soft: #3a3a40;
    --paper: #ffffff;
    --paper-tint: #eeeff1;
    --rule: #2b2b30;
  }
  * { box-sizing: border-box; margin: 0; padding: 0; }
  html, body {
    width: 1200px; height: 1031px; overflow: hidden;
    background: var(--page);
    font-family: "Libre Franklin", Arial, sans-serif;
  }
  .stage {
    width: 1200px; height: 1031px;
    display: flex; flex-direction: column; align-items: center; justify-content: center;
    gap: 56px;
  }
  .card {
    position: relative;
    width: 770px; height: 440px;
    border-radius: 26px;
    overflow: hidden;
    box-shadow: 0 10px 28px rgba(0,0,0,.18);
  }
  .card-artwork { position: absolute; inset: 0; }

  /* Front */
  .card--front { background: var(--blue-mid); color: var(--paper); }
  .card--front .card-artwork {
    background: radial-gradient(ellipse at 45% 55%, #4d86cf 0%, var(--blue-mid) 45%, var(--blue-deep) 100%);
  }
  .front-lockup {
    position: absolute; left: 0; right: 0; top: 140px;
    text-align: center;
  }
  .brand-name {
    font-weight: 800; font-size: 92px; letter-spacing: -3px; line-height: 1;
  }
  .brand-sub {
    margin-top: 10px;
    font-weight: 400; font-size: 18px; letter-spacing: 22px;
    padding-left: 22px;
  }
  .front-web {
    position: absolute; left: 0; right: 0; bottom: 56px;
    text-align: center; font-size: 26px; letter-spacing: 3px; font-weight: 400;
  }

  /* Back */
  .card--back { background: var(--paper); color: var(--ink); }
  .card--back .card-artwork {
    background: radial-gradient(ellipse at 75% 60%, var(--paper-tint) 0%, var(--paper) 70%);
  }
  .back-lockup { position: absolute; left: 56px; top: 60px; }
  .back-lockup .brand-name { font-size: 78px; color: var(--ink); }
  .back-lockup .brand-sub { font-size: 15px; letter-spacing: 18px; padding-left: 0; color: var(--ink); }
  .person { position: absolute; right: 56px; top: 176px; text-align: right; }
  .person-name { color: var(--blue-brand); font-weight: 600; font-size: 30px; }
  .person-title { color: var(--ink-soft); font-size: 17px; margin-top: 4px; }
  .divider {
    position: absolute; left: 56px; right: 56px; top: 250px;
    border-top: 1.5px solid var(--rule);
  }
  .contact-list { position: absolute; left: 56px; top: 276px; list-style: none; }
  .contact-list li {
    display: flex; align-items: center; gap: 12px;
    font-size: 21px; line-height: 1; margin-bottom: 14px; color: var(--ink);
  }
  .contact-list li.web { font-weight: 600; }
  .contact-icon {
    width: 22px; height: 22px; border-radius: 50%;
    background: var(--blue-brand);
    display: inline-flex; align-items: center; justify-content: center; flex: none;
  }
</style>
</head>
<body>
<main class="stage">

  <section class="card card--front" aria-label="Card front">
    <div class="card-artwork" role="img" aria-label="Blueprint-style engineering drawing of gears and dimension lines in white on blue"></div>
    <div class="front-lockup">
      <div class="brand-name">Forgeline</div>
      <div class="brand-sub">INTERNATIONAL</div>
    </div>
    <div class="front-web">ForgelineIntl.com</div>
  </section>

  <section class="card card--back" aria-label="Card back">
    <div class="card-artwork" role="img" aria-label="Faint grey engineering drawing of gears on white"></div>
    <div class="back-lockup">
      <div class="brand-name">Forgeline</div>
      <div class="brand-sub">INTERNATIONAL</div>
    </div>
    <div class="person">
      <div class="person-name">Dan Marlow</div>
      <div class="person-title">Senior Project Manager</div>
    </div>
    <div class="divider"></div>
    <ul class="contact-list">
      <li>
        <span class="contact-icon">
          <svg width="12" height="12" viewBox="0 0 24 24" fill="#fff"><path d="M6.6 10.8a15.1 15.1 0 0 0 6.6 6.6l2.2-2.2a1 1 0 0 1 1-.25 11.4 11.4 0 0 0 3.6.57 1 1 0 0 1 1 1V20a1 1 0 0 1-1 1A17 17 0 0 1 3 4a1 1 0 0 1 1-1h3.5a1 1 0 0 1 1 1c0 1.25.2 2.45.57 3.57a1 1 0 0 1-.25 1z"/></svg>
        </span>
        555-014-2200 xt 201
      </li>
      <li>
        <span class="contact-icon">
          <svg width="12" height="12" viewBox="0 0 24 24" fill="none" stroke="#fff" stroke-width="2.5"><rect x="3" y="6" width="18" height="12" rx="1"/><path d="M3 7l9 6 9-6"/></svg>
        </span>
        dan@forgelineintl.com
      </li>
      <li class="web">
        <span class="contact-icon">
          <svg width="12" height="12" viewBox="0 0 24 24" fill="none" stroke="#fff" stroke-width="2"><circle cx="12" cy="12" r="9"/><path d="M3 12h18M12 3c3 3 3 15 0 18M12 3c-3 3-3 15 0 18"/></svg>
        </span>
        ForgelineIntl.com
      </li>
    </ul>
  </section>

</main>
</body>
</html>
```